Online Marketing Agency Website

We are an online marketing agency that specializes in search marketing (SEM) for businesses of all sizes. Our core services include local search marketing, seo, paid search, paid social, graphic design, video production/editing and website design. We have an existing website that we launched a number of years ago but it's very outdated and we're currently too busy to design a new version.

Target Market(s)

Any business that needs online marketing services with an emphasis on search marketing.

Industry/Entity Type

Ad Agency

Number of Pages Required

4 page

Font styles to use
Sans Serif

Requirements
Must have
• Home page, interior page, blog page, contact us page.
Look and feel should be modern and clean and easy to navigate.
Sections for call outs for specific services: Business Marketing Strategy, Content Creation and Marketing, Graphic & Publication Design, Pay Per Click (PPC) Management, Search Engine Optimization, Social Media Management, Video Production & Editing, Website Hosting & Management, Website Design & Development
Use color from logo that was uploaded.

```html
<!DOCTYPE html>
<html lang="en">
<head>
<meta charset="utf-8">
<title>Lift Signal — Online Marketing Agency</title>
<link href="https://fonts.googleapis.com/css2?family=Poppins:wght@400;500;600;700&display=swap" rel="stylesheet">
<style>
:root{
  --orange:#ff4a17;
  --orange-soft:#ffe9e2;
  --dark:#2b2b2e;
  --darker:#232326;
  --ink:#1f1f24;
  --muted:#8a8a93;
  --line:#ececf0;
  --white:#ffffff;
  --bg-soft:#f7f7f9;
}
*{box-sizing:border-box;margin:0;padding:0}
html,body{width:1200px;height:3592px;overflow:hidden}
body{font-family:"Poppins",sans-serif;color:var(--ink);background:var(--white);position:relative}
.abs{position:absolute}

/* hero */
.hero{position:absolute;left:0;top:0;width:1200px;height:560px}
.hero-photo{position:absolute;inset:0;height:540px;background:linear-gradient(120deg,#3a3a40 0%,#5b5650 45%,#7d7168 70%,#4a4a4f 100%)}
.hero-photo::after{content:"";position:absolute;inset:0;background:rgba(20,20,24,.45)}
.nav{position:absolute;top:38px;left:160px;right:160px;display:flex;align-items:center;z-index:2}
.brand{display:flex;align-items:center;gap:10px;color:var(--white);font-weight:600;font-size:16px}
.brand-dot{width:18px;height:18px;border-radius:50%;background:var(--orange)}
.brand small{display:block;font-size:8px;font-weight:400;opacity:.8}
.menu{display:flex;gap:26px;margin-left:auto;margin-right:28px}
.menu a{color:var(--white);font-size:13px;text-decoration:none;font-weight:500}
.btn{display:inline-block;background:var(--orange);color:var(--white);font-weight:600;text-decoration:none;border-radius:30px}
.btn-login{font-size:12px;padding:9px 20px}
.hero-copy{position:absolute;left:160px;top:220px;z-index:2;color:var(--white)}
.hero-copy h1{font-size:40px;line-height:48px;font-weight:700;text-transform:uppercase}
.hero-copy p{font-size:13px;line-height:20px;width:300px;margin-top:16px;opacity:.9}
.btn-cta{font-size:13px;padding:14px 30px;margin-top:28px}
.hero-wave{position:absolute;left:0;top:400px;z-index:1}

/* about */
.eyebrow{font-size:10px;font-weight:600;color:var(--orange);text-transform:uppercase;letter-spacing:.5px}
.h2{font-size:30px;line-height:38px;font-weight:700;color:var(--ink)}
.about{position:absolute;left:160px;top:680px;width:880px;height:360px}
.about-text{position:absolute;left:0;top:30px;width:420px}
.about-text .h2{margin-top:10px}
.about-text p{font-size:12px;line-height:21px;color:var(--muted);margin-top:18px}
.about-photo{position:absolute;left:520px;top:0;width:280px;height:340px;background:linear-gradient(135deg,#d9d3cc,#a59b90 50%,#6d6660);}
.about-accent{position:absolute;left:500px;top:300px;width:60px;height:60px;background:var(--orange)}
.about-dots{position:absolute;left:480px;top:-20px;width:90px;height:90px;background-image:radial-gradient(var(--orange) 1.5px,transparent 1.5px);background-size:12px 12px;opacity:.5}
.mark{position:absolute;width:40px;height:40px;border-radius:50%;background:var(--white);box-shadow:0 4px 14px rgba(0,0,0,.12);display:flex;align-items:center;justify-content:center}
.mark span{width:14px;height:14px;border-radius:50%;background:var(--orange)}

/* services */
.services{position:absolute;left:0;top:1100px;width:1200px;height:820px;background:var(--bg-soft)}
.services-head{position:absolute;left:160px;top:60px}
.services-head .h2{margin-top:8px}
.services-head p{font-size:12px;line-height:20px;color:var(--muted);margin-top:10px;width:420px}
.service-grid{position:absolute;left:160px;top:220px;width:880px;display:grid;grid-template-columns:repeat(3,1fr);gap:28px 24px}
.service{background:var(--white);border-radius:6px;height:112px;display:flex;align-items:center;gap:18px;padding:0 26px;box-shadow:0 6px 20px rgba(0,0,0,.05)}
.service.active{border:1px solid var(--orange)}
.service svg{flex:none}
.service h3{font-size:14px;line-height:20px;font-weight:500}

/* work */
.work{position:absolute;left:160px;top:1980px;width:880px;height:460px}
.work .h2{margin-top:6px}
.tabs{position:absolute;right:0;top:24px;display:flex;gap:8px}
.tab{font-size:11px;padding:7px 16px;border-radius:4px;color:var(--ink);background:var(--white)}
.tab.on{background:var(--orange);color:var(--white)}
.work-grid{position:absolute;left:0;top:110px;display:flex;gap:28px}
.work-card{width:200px}
.work-img{width:200px;height:210px;border-radius:4px}
.work-card h4{font-size:12px;font-weight:500;margin-top:14px}
.work-card p{font-size:11px;color:var(--muted)}
.pager{position:absolute;left:400px;top:420px;display:flex;gap:6px}
.pager i{width:10px;height:4px;border-radius:2px;background:#f5b9a7}
.pager i.on{width:18px;background:var(--orange)}

/* testimonial */
.testimonial{position:absolute;left:0;top:2500px;width:1200px;height:320px;text-align:center}
.testimonial .h2{margin-top:6px}
.quote-mark{font-size:50px;line-height:40px;color:var(--ink);margin-top:18px;font-weight:700}
.testimonial blockquote{position:relative;z-index:1;width:560px;margin:12px auto 0;font-size:12px;line-height:20px;color:var(--muted);font-style:italic}
.client{display:flex;align-items:center;justify-content:center;gap:12px;margin-top:20px;text-align:left}
.avatar{border-radius:50%;background:linear-gradient(135deg,#c9c2bb,#8c837a)}
.client b{display:block;font-size:14px;font-weight:600}
.client small{font-size:11px;color:var(--muted)}

/* footer */
.footer-wave{position:absolute;left:0;top:2820px}
.footer{position:absolute;left:0;top:2940px;width:1200px;height:652px;background:var(--dark);color:var(--white)}
.contacts{position:absolute;left:160px;top:18px;width:880px;display:flex;align-items:center}
.contacts .brand{margin-right:auto}
.contact{display:flex;align-items:center;gap:10px;margin-left:48px}
.contact small{display:block;font-size:9px;color:#a5a5ad}
.contact b{font-size:12px;font-weight:500}
.foot-col{position:absolute;top:150px}
.foot-col h5{font-size:24px;font-weight:600}
.foot-list{display:grid;gap:14px 60px;margin-top:26px;list-style:none}
.foot-list li{font-size:11px;color:#c0c0c8}
.foot-bottom{position:absolute;left:160px;right:160px;top:560px;border-top:1px solid #3c3c42;padding-top:22px;display:flex;align-items:center}
.foot-bottom p{font-size:10px;color:#8e8e96}
.social{margin-left:auto;display:flex;gap:8px}
.social i{width:14px;height:14px;border-radius:50%;background:var(--orange);display:block}
</style>
</head>
<body>

<header class="hero">
  <div class="hero-photo" role="img" aria-label="Team of marketers smiling together in a bright office"></div>
  <nav class="nav">
    <div class="brand"><span class="brand-dot"></span><div>Lift Signal<small>Online Marketing Agency</small></div></div>
    <div class="menu"><a href="#">Custom Websites</a><a href="#">Existing Services</a><a href="#">Work</a><a href="#">Articles</a><a href="#">Contact</a></div>
    <a class="btn btn-login" href="#">Client Login</a>
  </nav>
  <div class="hero-copy">
    <h1>Custom Websites<br>That Convert Clients</h1>
    <p>Grow your brand with smart search marketing. Our team builds fast websites that turn visitors into loyal buyers.</p>
    <a class="btn btn-cta" href="#">GET STARTED</a>
  </div>
  <svg class="hero-wave" width="1200" height="160" viewBox="0 0 1200 160">
    <path d="M0 60 C250 150 520 160 760 110 C960 70 1080 40 1200 60 L1200 160 L0 160Z" fill="var(--orange)"/>
    <path d="M0 80 C250 170 520 175 760 128 C960 90 1080 62 1200 78 L1200 160 L0 160Z" fill="var(--white)"/>
  </svg>
</header>

<div class="mark" style="left:220px;top:640px"><span></span></div>

<section class="about">
  <div class="about-text">
    <div class="eyebrow">Who we are</div>
    <h2 class="h2">We Shape the Perfect<br>Solution for Company</h2>
    <p>Lift Signal is a full service online marketing agency. We handle every part of your digital growth, from search and paid ads to content and design, so you can focus on running your business while we bring in new leads and measurable results every single month.</p>
  </div>
  <div class="about-dots"></div>
  <div class="about-accent"></div>
  <div class="about-photo" role="img" aria-label="Colleagues working together around a laptop"></div>
</section>

<section class="services">
  <div class="services-head">
    <div class="eyebrow">What we offer</div>
    <h2 class="h2">Services we can help you with</h2>
    <p>Practical search marketing and creative work tailored to businesses of every size.</p>
  </div>
  <div class="service-grid">
    <div class="service"><svg width="34" height="34" viewBox="0 0 34 34" fill="none" stroke="var(--orange)" stroke-width="2"><rect x="4" y="8" width="26" height="18" rx="2"/><path d="M10 20l5-5 4 3 6-6"/></svg><h3>Business Marketing<br>Strategy</h3></div>
    <div class="service active"><svg width="34" height="34" viewBox="0 0 34 34" fill="none" stroke="var(--orange)" stroke-width="2"><rect x="6" y="4" width="22" height="26" rx="2"/><path d="M11 11h12M11 17h12M11 23h7"/></svg><h3>Content Creation &amp;<br>Marketing</h3></div>
    <div class="service"><svg width="34" height="34" viewBox="0 0 34 34" fill="none" stroke="var(--orange)" stroke-width="2"><path d="M6 28l4-10 14-14 6 6-14 14z"/><path d="M20 8l6 6"/></svg><h3>Graphic &amp;<br>Publication Design</h3></div>
    <div class="service"><svg width="34" height="34" viewBox="0 0 34 34" fill="none" stroke="var(--orange)" stroke-width="2"><path d="M8 4l18 12-8 2 5 9-4 2-5-9-6 5z"/></svg><h3>Pay Per Click (PPC)<br>Management</h3></div>
    <div class="service"><svg width="34" height="34" viewBox="0 0 34 34" fill="none" stroke="var(--orange)" stroke-width="2"><circle cx="14" cy="14" r="9"/><path d="M21 21l9 9"/></svg><h3>Search Engine<br>Optimization</h3></div>
    <div class="service"><svg width="34" height="34" viewBox="0 0 34 34" fill="none" stroke="var(--orange)" stroke-width="2"><circle cx="9" cy="17" r="4"/><circle cx="25" cy="8" r="4"/><circle cx="25" cy="26" r="4"/><path d="M12.5 15l9-5M12.5 19l9 5"/></svg><h3>Social Media<br>Management</h3></div>
    <div class="service"><svg width="34" height="34" viewBox="0 0 34 34" fill="none" stroke="var(--orange)" stroke-width="2"><rect x="3" y="8" width="20" height="18" rx="2"/><path d="M23 14l8-4v14l-8-4z"/></svg><h3>Video Production &amp;<br>Editing</h3></div>
    <div class="service"><svg width="34" height="34" viewBox="0 0 34 34" fill="none" stroke="var(--orange)" stroke-width="2"><rect x="5" y="5" width="24" height="10" rx="2"/><rect x="5" y="19" width="24" height="10" rx="2"/><path d="M10 10h2M10 24h2"/></svg><h3>Website Hosting &amp;<br>Management</h3></div>
    <div class="service"><svg width="34" height="34" viewBox="0 0 34 34" fill="none" stroke="var(--orange)" stroke-width="2"><rect x="3" y="6" width="28" height="20" rx="2"/><path d="M13 30h8M17 26v4M13 13l-3 3 3 3M21 13l3 3-3 3"/></svg><h3>Website Design &amp;<br>Development</h3></div>
  </div>
</section>

<section class="work">
  <div class="eyebrow">Our latest projects</div>
  <h2 class="h2">Some of Our Finest Work</h2>
  <div class="tabs"><span class="tab on">All</span><span class="tab">Branding</span><span class="tab">Web</span><span class="tab">Graphic</span></div>
  <div class="work-grid">
    <div class="work-card"><div class="work-img" role="img" aria-label="Product packaging pouch mockup" style="background:linear-gradient(160deg,#e9e7e4,#c9c3bc)"></div><h4>All Visions</h4><p>Web application</p></div>
    <div class="work-card"><div class="work-img" role="img" aria-label="Smart watch app design on a desk" style="background:linear-gradient(160deg,#f1efec,#9a9fa6)"></div><h4>All Visions</h4><p>Web application</p></div>
    <div class="work-card"><div class="work-img" role="img" aria-label="Tablet showing a colourful website design" style="background:linear-gradient(160deg,#6b8fb5,#e2a34b)"></div><h4>All Visions</h4><p>Web application</p></div>
    <div class="work-card"><div class="work-img" role="img" aria-label="Laptop screen with a landing page layout" style="background:linear-gradient(160deg,#a9bccf,#e6e9ee)"></div><h4>All Visions</h4><p>Web application</p></div>
  </div>
  <div class="pager"><i></i><i class="on"></i><i></i><i></i></div>
</section>

<section class="testimonial">
  <div class="avatar abs" style="left:210px;top:0;width:60px;height:60px" role="img" aria-label="Client portrait"></div>
  <div class="avatar abs" style="left:920px;top:10px;width:50px;height:50px" role="img" aria-label="Client portrait"></div>
  <div class="avatar abs" style="left:236px;top:200px;width:34px;height:34px" role="img" aria-label="Client portrait"></div>
  <div class="eyebrow">Testimonials</div>
  <h2 class="h2">What Our Client's Say</h2>
  <div class="quote-mark">&ldquo;</div>
  <blockquote>"Working with Lift Signal is always a pleasure, both personally and professionally. Their team brings real expertise and genuine care for what we do, and it shows in every result we see."</blockquote>
  <div class="client"><div class="avatar" style="width:38px;height:38px" role="img" aria-label="Client portrait"></div><div><b>Clara Denning</b><small>Head of Marketing</small></div></div>
</section>

<svg class="footer-wave" width="1200" height="130" viewBox="0 0 1200 130">
  <path d="M0 40 C300 120 600 130 880 70 C1010 42 1110 30 1200 40 L1200 130 L0 130Z" fill="var(--orange)"/>
  <path d="M0 62 C300 140 600 150 880 92 C1010 64 1110 52 1200 62 L1200 130 L0 130Z" fill="var(--dark)"/>
</svg>
<div class="mark" style="left:1030px;top:2820px"><span></span></div>

<footer class="footer">
  <div class="contacts">
    <div class="brand"><span class="brand-dot"></span><div>Lift Signal<small>Online Marketing Agency</small></div></div>
    <div class="contact"><svg width="22" height="22" viewBox="0 0 24 24" fill="none" stroke="var(--orange)" stroke-width="2"><path d="M5 3h4l2 5-3 2a12 12 0 0 0 6 6l2-3 5 2v4a2 2 0 0 1-2 2A18 18 0 0 1 3 5a2 2 0 0 1 2-2z"/></svg><div><small>Phone Number</small><b>0 800 5550 142</b></div></div>
    <div class="contact"><svg width="22" height="22" viewBox="0 0 24 24" fill="none" stroke="var(--orange)" stroke-width="2"><rect x="3" y="5" width="18" height="14" rx="2"/><path d="M3 7l9 6 9-6"/></svg><div><small>Email Address</small><b>info@liftsignal.com</b></div></div>
    <div class="contact"><svg width="22" height="22" viewBox="0 0 24 24" fill="none" stroke="var(--orange)" stroke-width="2"><path d="M12 22s7-7 7-12a7 7 0 0 0-14 0c0 5 7 12 7 12z"/><circle cx="12" cy="10" r="2.5"/></svg><div><small>Our Location</small><b>48 Harbor Lane, Springfield</b></div></div>
  </div>
  <div class="foot-col" style="left:160px">
    <h5>Services</h5>
    <ul class="foot-list" style="grid-template-columns:repeat(2,auto)">
      <li>Business Marketing Strategy</li><li>Search Engine Optimization</li>
      <li>Content Creation and Marketing</li><li>Social Media Management</li>
      <li>Graphic &amp; Publication Design</li><li>Video Production &amp; Editing</li>
      <li>Pay Per Click (PPC) Management</li><li>Website Hosting &amp; Management</li>
      <li></li><li>Website Design &amp; Development</li>
    </ul>
  </div>
  <div class="foot-col" style="left:800px">
    <h5>Support</h5>
    <ul class="foot-list" style="grid-template-columns:repeat(2,auto)">
      <li>Blog</li><li>Contact</li>
      <li>Case Studies</li><li>Privacy Policy</li>
      <li>Portfolio</li><li>Sitemap</li>
    </ul>
  </div>
  <div class="foot-bottom">
    <p>© 2024 Lift Signal Online Marketing. All rights reserved.</p>
    <div class="social"><i></i><i></i><i></i><i></i><i></i></div>
  </div>
</footer>

</body>
</html>
```